Business Card for innovative, tech/consultant company

We are specializing in bringing together Efficiency methodology and Technology for our Business customers. We would like an astonishing business Card that matches this idea.

Target Market(s)

Businesses of medium size or more

Industry/Entity Type

Business Consultant

Contact Information for Business Card

Name, Title, personal email, www, address, phone

Font styles to use
Sans Serif

Colors
3277b5

Requirements
Must have
• - innovative, efficient design
• - good readable
• - Colors must match our logo (blue and grey)
• - the attached font (is licensed by our Company) must be used (Syntax LT)
Should not have
• overloaded

```html
<!DOCTYPE html>
<html lang="en">
<head>
<meta charset="utf-8">
<title>Corevia Business Card</title>
<link rel="stylesheet" href="https://fonts.googleapis.com/css2?family=Source+Sans+3:wght@400;600;700&display=swap">
<style>
  :root {
    --backdrop: #1c1c1c;
    --card: #ffffff;
    --grey: #7f7f82;
    --blue: #3277b5;
    --blue-bright: #0a7cc4;
    --rule: #9a9a9a;
  }
  html, body {
    margin: 0;
    padding: 0;
    width: 1200px;
    height: 902px;
    overflow: hidden;
    background: var(--backdrop);
    font-family: "Source Sans 3", "Helvetica Neue", Arial, sans-serif;
  }
  .canvas {
    position: relative;
    width: 1200px;
    height: 902px;
  }
  .card {
    position: absolute;
    left: 99px;
    top: 165px;
    width: 902px;
    height: 514px;
    background: var(--card);
    border-radius: 24px;
  }
  .brand {
    position: absolute;
    left: 59px;
    top: 207px;
    width: 360px;
    height: 100px;
    display: flex;
    align-items: center;
  }
  .brand-name {
    font-size: 80px;
    font-weight: 600;
    line-height: 1;
    color: var(--blue);
  }
  .divider {
    position: absolute;
    left: 451px;
    top: 109px;
    width: 1.5px;
    height: 297px;
    background: var(--rule);
  }
  .details {
    position: absolute;
    left: 482px;
    top: 109px;
    color: var(--grey);
    white-space: nowrap;
  }
  .person-name {
    margin: 0;
    font-size: 42px;
    font-weight: 700;
    line-height: 34px;
    color: var(--grey);
  }
  .person-title {
    margin: 0;
    font-size: 30px;
    font-weight: 400;
    line-height: 33px;
    color: var(--blue-bright);
  }
  .address {
    margin: 29px 0 0;
    font-size: 30px;
    font-style: normal;
    line-height: 30px;
    color: var(--grey);
  }
  .contact-list {
    list-style: none;
    margin: 10px 0 0;
    padding: 0;
  }
  .contact-item {
    display: flex;
    align-items: center;
    gap: 16px;
    height: 30px;
    font-size: 30px;
    line-height: 30px;
    color: var(--grey);
  }
  .contact-icon {
    width: 24px;
    height: 24px;
    flex: none;
  }
  .website {
    margin: 10px 0 0;
    font-size: 31px;
    line-height: 32px;
    color: var(--blue-bright);
  }
</style>
</head>
<body>
<main class="canvas">
  <section class="card" aria-label="Business card">
    <div class="brand">
      <span class="brand-name">Corevia</span>
    </div>

    <div class="divider" aria-hidden="true"></div>

    <div class="details">
      <h1 class="person-name">Employee Name</h1>
      <p class="person-title">Managing Director</p>

      <address class="address">your address Rd., Suite 000<br>Fairhaven, USA</address>

      <ul class="contact-list">
        <li class="contact-item">
          <svg class="contact-icon" viewBox="0 0 24 24" aria-label="Mobile">
            <rect width="24" height="24" rx="4" fill="var(--blue-bright)"/>
            <rect x="7.5" y="3.5" width="9" height="17" rx="1.5" fill="none" stroke="#fff" stroke-width="1.6"/>
            <rect x="9.3" y="5.5" width="5.4" height="5" fill="#fff"/>
            <circle cx="12" cy="17.3" r="1" fill="#fff"/>
          </svg>
          <span>000.000.0000</span>
        </li>
        <li class="contact-item">
          <svg class="contact-icon" viewBox="0 0 24 24" aria-label="Phone">
            <rect width="24" height="24" rx="4" fill="var(--blue-bright)"/>
            <path d="M4 9.5c0-2.5 3.5-4 8-4s8 1.5 8 4v1.3h-4.2V9c-1-.6-2.4-.9-3.8-.9s-2.8.3-3.8.9v1.8H4z" fill="#fff"/>
            <path d="M7 12.5h10l1.5 6h-13z" fill="#fff"/>
            <circle cx="12" cy="15.3" r="1.6" fill="var(--blue-bright)"/>
          </svg>
          <span>000.000.0000</span>
        </li>
        <li class="contact-item">
          <svg class="contact-icon" viewBox="0 0 24 24" aria-label="Email">
            <rect width="24" height="24" rx="4" fill="var(--blue-bright)"/>
            <rect x="4" y="6.5" width="16" height="11" fill="#fff"/>
            <path d="M4.5 7l7.5 6 7.5-6" fill="none" stroke="var(--blue-bright)" stroke-width="1.4"/>
            <path d="M4.5 17l5.5-5M19.5 17l-5.5-5" fill="none" stroke="var(--blue-bright)" stroke-width="1.1"/>
          </svg>
          <span>info@youremail.com</span>
        </li>
      </ul>

      <p class="website">www.yourwebsite.com</p>
    </div>
  </section>
</main>
</body>
</html>
```